Business Cards and Stationary for a new consulting, recruiting and outsourcing company in Germany
BRAUNFELD Consulting
Business Cards and Stationary for a new consulting, recruiting and outsourcing company in Germany  - Consulting
Creative Brief
Professional
BRAUNFELD Consulting (Company Name) Ramune Braunfeld (First name, last name)
Inhaberin ("Owner" for english version)
Im Lindgrund 5 89512 Tannbach Deutschland ("Germany" for english version)
ramune.braunfeld@braunfeld-beratung.example
htttps://www.braunfeld-beratung.example
The round logo version with black background size around 75% of the card.

```html
<!DOCTYPE html>
<html lang="de">
<head>
<meta charset="utf-8">
<title>BRAUNFELD Consulting – Stationery</title>
<link href="https://fonts.googleapis.com/css2?family=Open+Sans:wght@400;600&display=swap" rel="stylesheet">
<style>
  :root{
    --cyan:#1ea9e8;
    --magenta:#e6157f;
    --ink:#6d6e70;
    --text:#8a8b8d;
    --paper:#ffffff;
    --stage:#eceeef;
    --black:#0d0d0f;
  }
  *{box-sizing:border-box;margin:0;padding:0}
  html,body{width:1200px;height:936px;overflow:hidden}
  body{background:var(--stage);font-family:"Open Sans",Arial,sans-serif;position:relative;color:var(--text)}
  .sheet{position:absolute;background:var(--paper);overflow:hidden}
  .swoosh{position:absolute;inset:0;width:100%;height:100%}
  .brand{position:absolute;display:flex;align-items:center;gap:6px;white-space:nowrap}
  .brand-dot{border-radius:50%;background:var(--cyan);flex:none}
  .brand-name{color:var(--ink);font-weight:400}

  /* Letterhead */
  .letterhead{left:182px;top:68px;width:388px;height:552px}
  .letterhead .brand{left:36px;top:36px}
  .letterhead .brand-dot{width:22px;height:22px}
  .letterhead .brand-name{font-size:12px}
  .letter-contact{position:absolute;right:34px;top:34px;font-size:4.6px;line-height:7px;width:110px}
  .letter-body{position:absolute;left:36px;top:112px;width:260px;font-size:5px;line-height:7.6px}
  .letter-body p{margin-bottom:9px}
  .signature{display:block;width:40px;height:1px;background:var(--text);margin:6px 0 8px}

  /* Folder */
  .folder{left:628px;top:46px;width:405px;height:569px}
  .folder .brand{left:118px;top:254px}
  .folder .brand-dot{width:36px;height:36px}
  .folder .brand-name{font-size:17px}
  .folder-url{position:absolute;right:28px;bottom:32px;color:#fff;font-size:7.5px;letter-spacing:.8px}

  /* Business cards */
  .card-front{left:33px;top:653px;width:190px;height:88px}
  .card-front .brand{left:10px;top:10px;gap:4px}
  .card-front .brand-dot{width:12px;height:12px}
  .card-front .brand-name{font-size:6.4px}
  .card-details{position:absolute;left:10px;top:40px;font-size:3.6px;line-height:5.2px;color:var(--ink)}
  .card-details strong{font-weight:600;font-size:4.4px}
  .card-back{left:33px;top:759px;width:190px;height:91px;background:var(--black)}
  .card-back .brand{left:50%;top:50%;transform:translate(-50%,-50%);gap:6px}
  .card-back .brand-dot{width:26px;height:26px}
  .card-back .brand-name{color:#fff;font-size:9px}

  /* Envelopes */
  .envelope-front{left:261px;top:663px;width:455px;height:213px}
  .envelope-front .brand{left:36px;top:28px}
  .envelope-front .brand-dot{width:22px;height:22px}
  .envelope-front .brand-name{font-size:12px}
  .envelope-back{left:739px;top:666px;width:415px;height:197px}
  .envelope-flap{position:absolute;left:0;top:0;width:100%;height:44px;background:var(--cyan)}
  .envelope-url{position:absolute;right:26px;top:16px;color:#fff;font-size:7px;letter-spacing:.8px}
</style>
</head>
<body>

<section class="sheet letterhead">
  <svg class="swoosh" viewBox="0 0 388 552" preserveAspectRatio="none" aria-hidden="true">
    <path d="M388,330 C380,440 320,510 250,552 L388,552 Z" fill="var(--cyan)"/>
    <path d="M388,300 C392,400 360,480 320,552 L332,552 C372,490 388,420 388,360 Z" fill="var(--paper)"/>
    <path d="M388,250 C386,330 380,370 376,400 C388,380 388,350 388,330 Z" fill="var(--magenta)"/>
  </svg>
  <div class="brand"><span class="brand-dot"></span><span class="brand-name">BRAUNFELD Consulting</span></div>
  <div class="letter-contact">
    Im Lindgrund 5<br>89512 Tannbach<br>ramune.braunfeld@braunfeld-beratung.example<br>htttps://www.braunfeld-beratung.example
  </div>
  <div class="letter-body">
    <p>12 May 2024</p>
    <p>Herr Jonas Keller<br>Hauptstraße 14, 80331 München</p>
    <p>Thank you for your interest in our consulting services. We support growing companies with recruiting, outsourcing and strategic advice, tailored to your goals and timelines.</p>
    <p>Our team combines local knowledge with international experience to build strong teams and efficient processes that deliver results you can measure.</p>
    <p>We look forward to discussing how we can help your business move forward. Please contact us at any time to arrange a first meeting.</p>
    <p>Kind regards,<span class="signature"></span>Ramune Braunfeld<br>Inhaberin</p>
  </div>
</section>

<section class="sheet folder">
  <svg class="swoosh" viewBox="0 0 405 569" preserveAspectRatio="none" aria-hidden="true">
    <path d="M330,0 C440,180 340,440 150,569 L405,569 L405,0 Z" fill="var(--cyan)"/>
    <path d="M300,0 L405,0 L405,160 C395,90 360,35 300,0 Z" fill="var(--magenta)"/>
  </svg>
  <div class="brand"><span class="brand-dot"></span><span class="brand-name">BRAUNFELD Consulting</span></div>
  <div class="folder-url">www.braunfeld-beratung.example</div>
</section>

<section class="sheet card-front">
  <svg class="swoosh" viewBox="0 0 190 88" preserveAspectRatio="none" aria-hidden="true">
    <path d="M190,10 C170,50 140,75 110,88 L190,88 Z" fill="var(--cyan)"/>
    <path d="M190,0 L190,22 C182,12 176,5 170,0 Z" fill="var(--magenta)"/>
  </svg>
  <div class="brand"><span class="brand-dot"></span><span class="brand-name">BRAUNFELD Consulting</span></div>
  <div class="card-details">
    <strong>Ramune Braunfeld</strong><br>Inhaberin<br>Im Lindgrund 5, 89512 Tannbach<br>ramune.braunfeld@braunfeld-beratung.example<br>htttps://www.braunfeld-beratung.example
  </div>
</section>

<section class="sheet card-back">
  <div class="brand"><span class="brand-dot"></span><span class="brand-name">BRAUNFELD Consulting</span></div>
</section>

<section class="sheet envelope-front">
  <svg class="swoosh" viewBox="0 0 455 213" preserveAspectRatio="none" aria-hidden="true">
    <path d="M455,40 C430,130 380,185 320,213 L455,213 Z" fill="var(--cyan)"/>
    <path d="M455,0 L455,70 C450,40 440,15 425,0 Z" fill="var(--magenta)"/>
  </svg>
  <div class="brand"><span class="brand-dot"></span><span class="brand-name">BRAUNFELD Consulting</span></div>
</section>

<section class="sheet envelope-back">
  <svg class="swoosh" viewBox="0 0 415 197" preserveAspectRatio="none" aria-hidden="true">
    <path d="M0,44 L207,120 L415,44" fill="none" stroke="#e3e5e7" stroke-width="1"/>
  </svg>
  <div class="envelope-flap"></div>
  <div class="envelope-url">www.braunfeld-beratung.example</div>
</section>

</body>
</html>
```